Industrial Project Sign

We need an eye catching (but professional) industrial project sign that will be very large (roughly 12' high x 18' wide). This sign will be highly visible from the adjacent high speed highway.

* The following needs to be at the bottom of the signage: Logo (uploaded), Name (Pillar Ventures Group, Inc.) (uploaded) and phone number (555)613-8874

*Name of Project - "Brambleford Industrial Center"

* Text items
Land for Sale
Build to Suit
Zoning: Industrial (G I & L I)

* Interesting background that is eye catching
Updates

Good morning all,

We are considering all designers options as we go and are waiting for the final designs to come in by the 4th so that we can give each one a good look.   If you have any new designs, questions, further design options or any tweeks you want to do to current designs, please do so at this time.

Thanks to all of you for your submissions.

Industry/Entity Type

Industrial

```html
<!DOCTYPE html>
<html lang="en">
<head>
<meta charset="utf-8">
<title>Brambleford Industrial Center — Project Sign</title>
<link href="https://fonts.googleapis.com/css2?family=Anton&family=Alfa+Slab+One&family=Arimo:wght@400;700&display=swap" rel="stylesheet">
<style>
  :root {
    --sky-top: #b3d3ee;
    --sky-bottom: #5aa8dc;
    --tan-light: #f1dcb8;
    --tan-mid: #e2bb86;
    --tan-dark: #c8914f;
    --panel-edge: #a87c4f;
    --title-fill: #fff200;
    --ink: #111111;
    --green: #23643a;
    --green-edge: #0d2a17;
    --maroon: #7e1616;
  }
  html, body {
    margin: 0;
    padding: 0;
    width: 1200px;
    height: 927px;
    overflow: hidden;
    background: #ffffff;
  }
  .sign {
    display: block;
    width: 1200px;
    height: 927px;
  }
  .project-title {
    font-family: "Anton", "Impact", sans-serif;
    font-size: 100px;
    fill: var(--title-fill);
    stroke: var(--ink);
    stroke-width: 4px;
    paint-order: stroke fill;
  }
  .offer {
    font-family: "Alfa Slab One", "Georgia", serif;
    font-size: 44px;
    fill: var(--green);
    stroke: var(--green-edge);
    stroke-width: 1.5px;
    paint-order: stroke fill;
  }
  .zoning {
    font-family: "Alfa Slab One", "Georgia", serif;
    font-size: 44px;
    fill: var(--ink);
  }
  .company-name {
    font-family: "Arimo", "Arial", sans-serif;
    font-size: 28px;
    fill: var(--ink);
  }
  .phone {
    font-family: "Arimo", "Arial", sans-serif;
    font-weight: 700;
    font-size: 40px;
    fill: var(--ink);
  }
</style>
</head>
<body>
<svg class="sign" viewBox="0 0 1200 927" xmlns="http://www.w3.org/2000/svg" role="img" aria-label="Brambleford Industrial Center sign: Land For Sale, Build to Suit, Zoning Industrial (GI &amp; LI), Pillar Ventures Group, Inc., (555) 613-8874">
  <defs>
    <linearGradient id="sky" x1="0" y1="0" x2="0" y2="1">
      <stop offset="0" stop-color="var(--sky-top)"/>
      <stop offset="0.4" stop-color="var(--sky-bottom)"/>
      <stop offset="1" stop-color="var(--sky-bottom)"/>
    </linearGradient>
    <linearGradient id="metal-tan" x1="0" y1="0" x2="1" y2="0">
      <stop offset="0" stop-color="var(--tan-mid)"/>
      <stop offset="0.2" stop-color="var(--tan-light)"/>
      <stop offset="0.45" stop-color="var(--tan-mid)"/>
      <stop offset="0.7" stop-color="var(--tan-light)"/>
      <stop offset="1" stop-color="var(--tan-mid)"/>
    </linearGradient>
  </defs>

  <rect class="sky" x="0" y="0" width="1200" height="927" fill="url(#sky)"/>

  <rect class="ground-panel" x="0" y="300" width="1200" height="627"
        fill="url(#metal-tan)" stroke="var(--panel-edge)" stroke-width="3"
        role="img" aria-label="Industrial building skyline silhouette in tan"/>

  <text class="project-title" x="20" y="165" textLength="1160" lengthAdjust="spacingAndGlyphs">Brambleford Industrial Center</text>

  <text class="offer" x="72" y="485" textLength="402" lengthAdjust="spacingAndGlyphs">Land For Sale</text>
  <text class="offer" x="738" y="485" textLength="378" lengthAdjust="spacingAndGlyphs">Build to Suit</text>

  <text class="zoning" x="148" y="615" textLength="872" lengthAdjust="spacingAndGlyphs">Zoning:  Industrial (GI  &amp;  LI)</text>

  <rect class="company-mark" x="40" y="752" width="120" height="120" fill="var(--maroon)"/>
  <text class="company-name" x="222" y="822" textLength="414" lengthAdjust="spacingAndGlyphs">Pillar Ventures Group, Inc.</text>
  <line class="company-rule" x1="213" y1="836" x2="636" y2="836" stroke="var(--maroon)" stroke-width="4"/>

  <text class="phone" x="850" y="838" textLength="316" lengthAdjust="spacingAndGlyphs">(555) 613-8874</text>
</svg>
</body>
</html>
```